Business Card Design Project

Colette Marivaux logo on front of card with 'of Sydney' added in small font.
Back of card needs to include the following information :

"Pure pleasure for the discerning gentleman" (I may omit once I've seen the design)

colettemarivaux.com.au

Contact by SMS or email only :

colette@colettemarivaux.com.au
Mobile : 0483 956 204 or + 61 483 956 204

Target Market(s)

Male professionals aged 20-60.

Industry/Entity Type

Business

Requirements
Must have
• Simple, bold, stylish and elegant.

```html
<!DOCTYPE html>
<html lang="en">
<head>
<meta charset="utf-8">
<title>Colette Marivaux of Sydney — Business Card</title>
<link rel="stylesheet" href="https://fonts.googleapis.com/css2?family=Alegreya:wght@500&family=Open+Sans:wght@400&family=Pinyon+Script&display=swap">
<style>
  :root {
    --ink: #000000;
    --paper: #ffffff;
    --stone: #c0beb2;
  }
  * { margin: 0; padding: 0; box-sizing: border-box; }
  html, body {
    width: 844px;
    height: 1200px;
    overflow: hidden;
    background: var(--stone);
  }
  .card {
    position: relative;
    width: 844px;
    height: 1200px;
    background: var(--stone);
  }
  .front {
    position: absolute;
    left: 0; top: 0;
    width: 844px; height: 425px;
    background: var(--ink);
    box-shadow: inset 0 0 10px 4px rgba(60,60,60,0.8);
    display: flex;
    align-items: center;
    justify-content: center;
  }
  .brand-name {
    font-family: "Alegreya", serif;
    font-weight: 500;
    font-size: 72px;
    color: var(--paper);
    letter-spacing: 1px;
    margin-top: -10px;
  }
  .city-band {
    position: absolute;
    left: 0; top: 465px;
    width: 844px; height: 110px;
    background: var(--ink);
    color: var(--paper);
    font-family: "Open Sans", sans-serif;
    font-size: 46px;
    display: flex;
    align-items: center;
    justify-content: center;
    letter-spacing: 1px;
  }
  .divider {
    position: absolute;
    left: 0; top: 575px;
    width: 844px; height: 50px;
    background: var(--paper);
  }
  .back {
    position: absolute;
    left: 22px; top: 650px;
    width: 796px; height: 518px;
    background: var(--ink);
    color: var(--paper);
    font-family: "Alegreya", serif;
    font-weight: 500;
  }
  .tagline {
    position: absolute;
    left: 0; top: 30px;
    width: 100%;
    text-align: center;
    font-family: "Pinyon Script", cursive;
    font-size: 44px;
    font-weight: 400;
    -webkit-text-stroke: 1px var(--paper);
  }
  .website {
    position: absolute;
    left: 0; top: 115px;
    width: 100%;
    text-align: center;
    font-size: 35px;
  }
  .contact {
    position: absolute;
    left: 116px; top: 232px;
    font-size: 36px;
    line-height: 56px;
  }
  .contact .note { margin-bottom: 10px; }
  .contact .intl { padding-left: 146px; }
</style>
</head>
<body>
  <div class="card">
    <section class="front">
      <div class="brand-name">Colette Marivaux</div>
    </section>

    <div class="city-band">OF SYDNEY</div>
    <div class="divider"></div>

    <section class="back">
      <p class="tagline">Pure pleasure for deserning gentleman</p>
      <p class="website">colettemarivaux.com.au</p>
      <div class="contact">
        <p class="note">Contact by SMS or email only :</p>
        <p class="email">colette@colettemarivaux.com.au</p>
        <p class="mobile">Mobile : 0483 956 204 or</p>
        <p class="intl">+ 61 483 956 204</p>
      </div>
    </section>
  </div>
</body>
</html>
```